Business card for a doctor's practice

Would like a business card for a Pulmonary ( lung) doctor. I would like to include a logo with something in reference to air or oxygen or lungs. Would like the color red included somehow. Name of the company is Breathwell Medical Associates of Eastern Ridgeford and we specialize in Pulmonary Medicine,. I would like something streamlined and modern
Target Market(s)
Patients, hospitals, other doctors
Industry/Entity Type
Business
Contact Information for Business Card
Would like business details superimposed on a logo somehow

```html
<!DOCTYPE html>
<html lang="en">
<head>
<meta charset="utf-8">
<title>Breathwell Medical Associates – Business Card</title>
<link rel="stylesheet" href="https://fonts.googleapis.com/css2?family=Comfortaa:wght@500;700&family=Open+Sans:wght@700&display=swap">
<style>
  :root {
    --brand-red: #ed1c24;
    --paper: #ffffff;
    --ink-light: #ffffff;
    --card-edge: #e0262c;
  }
  html, body {
    margin: 0;
    padding: 0;
    width: 1200px;
    height: 652px;
    overflow: hidden;
    background: var(--paper);
  }
  .card {
    position: relative;
    width: 1200px;
    height: 652px;
    display: flex;
    box-sizing: border-box;
    border: 1px solid var(--card-edge);
  }
  .brand-side {
    width: 599px;
    height: 100%;
    background: var(--paper);
    position: relative;
  }
  .brand-mark {
    position: absolute;
    left: 234px;
    top: 178px;
    width: 132px;
    height: 132px;
    background: var(--brand-red);
  }
  .brand-name {
    position: absolute;
    left: 0;
    width: 599px;
    top: 392px;
    margin: 0;
    text-align: center;
    font-family: "Comfortaa", sans-serif;
    font-weight: 700;
    font-size: 30px;
    line-height: 40px;
    letter-spacing: 1px;
    text-transform: uppercase;
    color: var(--brand-red);
  }
  .contact-side {
    flex: 1;
    height: 100%;
    background: var(--brand-red);
    color: var(--ink-light);
    position: relative;
    text-align: center;
  }
  .person-name {
    position: absolute;
    left: 0;
    right: 0;
    top: 146px;
    margin: 0;
    font-family: "Open Sans", sans-serif;
    font-weight: 700;
    font-size: 50px;
    line-height: 60px;
    text-shadow: 2px 3px 4px rgba(90, 0, 0, 0.55);
  }
  .person-role {
    position: absolute;
    left: 0;
    right: 0;
    top: 210px;
    margin: 0;
    font-family: "Open Sans", sans-serif;
    font-weight: 700;
    font-size: 29px;
    line-height: 36px;
    text-shadow: 2px 2px 3px rgba(90, 0, 0, 0.5);
  }
  .contact-list {
    position: absolute;
    left: 0;
    right: 0;
    top: 392px;
    margin: 0;
    padding: 0;
    list-style: none;
    font-family: "Comfortaa", sans-serif;
    font-weight: 500;
    font-size: 24px;
    line-height: 37px;
    text-shadow: 1px 2px 3px rgba(90, 0, 0, 0.45);
  }
</style>
</head>
<body>
  <main class="card">
    <section class="brand-side">
      <div class="brand-mark"></div>
      <p class="brand-name">Breathwell Medical<br>Associates of<br>Eastern Ridgeford</p>
    </section>
    <section class="contact-side">
      <h1 class="person-name">DANIEL R. HAYES</h1>
      <p class="person-role">General Manager</p>
      <ul class="contact-list">
        <li>Harbor Road, Linden Street,</li>
        <li>40512, Eastgate, Ridgeford</li>
        <li>555 00 00 - 555 01 01</li>
        <li>info@breathwellmed.example</li>
        <li>www.breathwellmed.example</li>
      </ul>
    </section>
  </main>
</body>
</html>
```